Atelier Marrow Architecture business card

We need to update our business card. We do high end custom residential, hospitality, and wellness architecture. We focus on creating unique spaces and design around the five senses, believing that architecture's true impact is not on our surroundings, but within us. We would like to see designs are instill a sense of calm awe. They should be crisp, fresh, clean, authentic, & contemporary without being sterile, overworked, or harsh. White space is important. Alternative materials are an option if natural. We have created our own logo and would like designs to incorporate it. However, we are willing to see alternatives if the logo becomes a stumbling block and you have an alternate you suggest. Card must have the following information:
Atelier Marrow Architecture, Inc.
728 Holloway Ct. NE Atlanta, GA 30318
Marcus T. Whitcombe, AIA, NCARB, LEED AP BD+C
ateliermarrow.example

Target Market(s)

Higher net worth individuals with an appreciation for design, nature, sustainability,

Industry/Entity Type

Architect

Contact Information for Business Card

See above. The title of Owner or Architect is helpful but not necessary. Minimalism should trump additional information.

Font styles to use
Serif
Sans Serif

Requirements
Must have
• It should look professional. It must use logo
Should not have
• caligraphy, animals, anything that is cute,

```html
<!DOCTYPE html>
<html lang="en">
<head>
<meta charset="utf-8">
<title>Atelier Marrow Architecture — Business Card</title>
<link rel="stylesheet" href="https://fonts.googleapis.com/css2?family=DM+Sans:wght@400;500;700&display=swap">
<style>
  :root {
    --backdrop: #5a4939;
    --paper: #ffffff;
    --forest: #00573f;
    --charcoal: #434343;
    --ink: #3a3a3a;
    --rule: #9a9a9a;
    --shadow: rgba(0, 0, 0, 0.45);
  }
  * { box-sizing: border-box; margin: 0; padding: 0; }
  html, body {
    width: 1200px;
    height: 987px;
    overflow: hidden;
    background: var(--backdrop);
    font-family: "DM Sans", Arial, sans-serif;
  }
  .canvas {
    position: relative;
    width: 1200px;
    height: 987px;
  }
  .card {
    position: absolute;
    left: 293px;
    width: 615px;
    height: 342px;
    box-shadow: 0 3px 8px var(--shadow);
  }
  /* Front */
  .card--front {
    top: 130px;
    background: var(--paper);
    border-top: 9px solid var(--charcoal);
    border-bottom: 7px solid var(--forest);
  }
  .wordmark {
    position: absolute;
    font-family: "DM Sans", Arial, sans-serif;
    font-weight: 400;
    text-transform: uppercase;
    letter-spacing: 0.32em;
    white-space: nowrap;
  }
  .card--front .wordmark {
    top: 56px;
    right: 26px;
    font-size: 17px;
    color: var(--forest);
  }
  .person {
    position: absolute;
    left: 31px;
    top: 193px;
    color: var(--forest);
  }
  .person__name {
    font-size: 23px;
    font-weight: 700;
    letter-spacing: 0.01em;
    text-transform: uppercase;
    line-height: 1;
  }
  .person__credentials {
    margin-top: 7px;
    font-size: 14px;
    font-weight: 400;
    letter-spacing: 0.02em;
    line-height: 1;
  }
  .divider {
    position: absolute;
    left: 32px;
    right: 25px;
    top: 245px;
    height: 1px;
    background: var(--rule);
  }
  .address {
    position: absolute;
    left: 32px;
    top: 262px;
    font-size: 15px;
    line-height: 23px;
    color: var(--ink);
    text-transform: uppercase;
    font-style: normal;
  }
  .website {
    position: absolute;
    right: 25px;
    top: 285px;
    font-size: 15px;
    line-height: 23px;
    letter-spacing: 0.1em;
    color: var(--ink);
    text-transform: uppercase;
  }
  /* Back */
  .card--back {
    top: 506px;
    height: 351px;
    background: var(--forest);
    display: flex;
    align-items: center;
    justify-content: center;
  }
  .card--back .wordmark {
    position: static;
    font-size: 20px;
    color: var(--paper);
  }
</style>
</head>
<body>
<main class="canvas">
  <section class="card card--front" aria-label="Business card front">
    <div class="wordmark">Atelier Marrow Architecture</div>
    <div class="person">
      <h1 class="person__name">Marcus T. Whitcombe</h1>
      <p class="person__credentials">AIA, NCARB, LEED AP BD+C</p>
    </div>
    <div class="divider"></div>
    <address class="address">728 Holloway Ct.<br>NE Atlanta, GA 30318</address>
    <p class="website">www.ateliermarrow.example</p>
  </section>
  <section class="card card--back" aria-label="Business card back">
    <div class="wordmark">Atelier Marrow Architecture</div>
  </section>
</main>
</body>
</html>
```